Domain Parking page and Listing page

1)
In need a design of a domain parking page, mainly with the same features as VORIQ.com as can be seen here: https://wanderplum.com/

2)
I need a design of a website with all domains listed. There's no company logo/name yet so it should be in plain font, for example "tilmorex.site" (this is just an example), similar as:
https://voriq.com/search?&terms=park&results=50&order_by=relevance

Delivery after approval in HTML/CSS. Should be responsive. Ideally use a framework like Bootstrap

Target Market(s)

Domain buyers, business owners

Industry/Entity Type

Business to business, Marketing, domains

Coding

Coded - Design and coding required

Number of Pages Required

2 page

Font styles to use
Sans Serif

Requirements
Must have
• Responsive design, worldly design.

```html
<!DOCTYPE html>
<html lang="en">
<head>
<meta charset="utf-8">
<title>tilmorex.site — Homepage and Listing</title>
<link href="https://fonts.googleapis.com/css2?family=Poppins:wght@400;500;600;700&display=swap" rel="stylesheet">
<style>
:root{
  --board-top:#6fd3f0;
  --board-bottom:#2b9fe0;
  --navy:#0b1a4d;
  --navy-deep:#06113a;
  --blue:#1e5bff;
  --blue-soft:#3f86ff;
  --ink:#1a2350;
  --muted:#7a84a6;
  --line:#e3e8f4;
  --white:#ffffff;
  --green:#21c07a;
  --orange:#f5a524;
}
*{margin:0;padding:0;box-sizing:border-box}
html,body{width:753px;height:1200px;overflow:hidden}
body{font-family:"Poppins",sans-serif;color:var(--ink);
  background:linear-gradient(160deg,var(--board-top),var(--board-bottom));position:relative}
.board-title{position:absolute;top:84px;left:0;width:100%;text-align:center;color:var(--white);font-size:40px;font-weight:700;letter-spacing:.5px}
.board-label{position:absolute;top:176px;color:var(--white);font-size:17px;font-weight:500}
.label-home{left:45px}
.label-listing{left:402px}
.page{position:absolute;background:var(--white);overflow:hidden;box-shadow:0 10px 30px rgba(6,17,58,.3)}
.page-home{left:45px;top:200px;width:296px;height:960px}
.page-listing{left:402px;top:200px;width:288px;height:670px}
.abs{position:absolute}
.dark{background:radial-gradient(circle at 70% 30%,#1b3a9a,var(--navy) 55%,var(--navy-deep))}
.nav{position:absolute;top:8px;left:12px;right:12px;display:flex;align-items:center;gap:8px;font-size:4px;color:#c9d4ff}
.nav-logo{font-weight:700;font-size:5px;color:var(--white);margin-right:auto;letter-spacing:.3px}
.nav-btn{background:var(--blue);color:var(--white);padding:2px 7px;border-radius:2px}
.wave{position:absolute;left:0;width:100%}
.btn{display:inline-block;background:var(--blue);color:var(--white);font-size:4px;font-weight:500;padding:3px 8px;border-radius:2px}
.art{position:absolute;border-radius:6px}
h2.section-title{font-size:10px;font-weight:700;color:var(--ink);line-height:1.2}
h2.section-title .accent{color:var(--blue)}
.copy{font-size:3.6px;color:var(--muted);line-height:1.5}
/* hero */
.hero{top:0;left:0;width:296px;height:160px}
.hero-title{position:absolute;top:38px;left:16px;font-size:11px;font-weight:600;color:var(--white);line-height:1.25}
.hero-copy{position:absolute;top:68px;left:16px;width:110px;color:#aab6e6}
.hero-search{position:absolute;top:84px;left:16px;width:100px;height:10px;background:var(--white);border-radius:2px}
.hero-search .btn{position:absolute;right:1px;top:1px;padding:1px 5px;font-size:3.5px}
.hero-art{top:26px;left:168px;width:112px;height:84px;background:radial-gradient(circle at 50% 60%,#6a5cff,#2d4fd6 55%,transparent 75%)}
/* features */
.features{top:172px;left:0;width:296px;display:flex;justify-content:center;align-items:flex-end;gap:8px}
.feature{width:70px;height:64px;background:var(--white);border-radius:4px;box-shadow:0 4px 12px rgba(30,60,140,.15);text-align:center;padding-top:14px}
.feature-main{height:82px;background:var(--blue);color:var(--white)}
.feature .icon{width:12px;height:12px;margin:0 auto 6px;border-radius:3px}
.feature h3{font-size:4.4px;font-weight:600}
.feature p{font-size:3.2px;color:var(--muted);margin-top:2px;padding:0 6px}
.feature-main p{color:#d8e2ff}
.features-cta{top:270px;left:0;width:296px;text-align:center}
/* buy sell */
.trade-art{top:325px;left:18px;width:100px;height:88px;background:linear-gradient(135deg,#4b6bff,#2535b8)}
.trade-text{top:325px;left:132px;width:148px}
.trade-item{display:flex;gap:5px;margin-top:7px}
.trade-item .dot{width:9px;height:9px;border-radius:2px;flex:none}
.trade-item h4{font-size:4.2px;font-weight:600}
/* investors */
.investors{top:520px;left:0;width:296px;text-align:center}
.investors .copy{width:170px;margin:4px auto 6px}
.investors-art{top:578px;left:58px;width:180px;height:140px;background:radial-gradient(circle at 50% 55%,#c9d3ff,#eef2ff 70%,transparent)}
/* home footer */
.home-footer{top:720px;left:0;width:296px;height:240px}
.cta-title{position:absolute;top:58px;left:16px;font-size:10px;font-weight:700;color:var(--white)}
.cta-title .accent{color:var(--blue-soft)}
.cta-copy{position:absolute;top:74px;left:16px;width:120px;color:#aab6e6}
.cta-btn{position:absolute;top:90px;left:16px}
.cta-art{top:18px;left:180px;width:96px;height:100px;background:linear-gradient(180deg,#5d7bff,#2c3fc4)}
.foot-cols{position:absolute;top:140px;left:16px;right:16px;display:flex;justify-content:space-between}
.foot-col h5{font-size:4px;color:var(--white);font-weight:600;margin-bottom:3px}
.foot-col p{font-size:3.4px;color:#8e9bcc;line-height:1.7}
.socials{display:flex;gap:3px;margin-top:2px}
.socials span{width:5px;height:5px;border-radius:50%;background:#8e9bcc}
.foot-bar{position:absolute;bottom:10px;left:16px;right:16px;border-top:.5px solid #2a3a7a;padding-top:5px;display:flex;justify-content:space-between;font-size:3.2px;color:#8e9bcc}
/* listing */
.list-header{top:0;left:0;width:288px;height:110px}
.list-search{position:absolute;top:42px;left:30px;width:228px;height:11px;background:var(--white);border-radius:2px}
.list-search .btn{position:absolute;right:1px;top:1px;padding:1.5px 8px;font-size:3.5px}
.filters{top:122px;left:16px;width:82px}
.filter{margin-bottom:14px}
.filter h5{font-size:4.4px;font-weight:600;margin-bottom:4px}
.filter-row{display:flex;align-items:center;gap:3px;font-size:3.4px;color:var(--muted);margin-bottom:2.5px}
.filter-row .box{width:4px;height:4px;border:.5px solid var(--muted);border-radius:1px}
.filter-row .box.on{background:var(--blue);border-color:var(--blue)}
.range{height:2px;background:var(--line);border-radius:1px;position:relative;margin:4px 0 6px}
.range::before{content:"";position:absolute;left:10%;right:35%;top:0;bottom:0;background:var(--blue)}
.field{height:7px;border:.5px solid var(--line);border-radius:1.5px;margin-bottom:3px;font-size:3.2px;color:var(--muted);padding:1.2px 3px}
.results{top:122px;left:108px;width:166px}
.results-head{display:flex;justify-content:space-between;font-size:4.2px;font-weight:600;margin-bottom:6px}
.results-head span{color:var(--muted);font-weight:400}
.result{display:flex;justify-content:space-between;align-items:center;border-bottom:.5px solid var(--line);padding:6px 0}
.result h6{font-size:4.4px;font-weight:600}
.result p{font-size:3.2px;color:var(--muted)}
.result .btn{padding:2px 9px;font-size:3.5px}
.list-footer{top:560px;left:0;width:288px;height:110px}
</style>
</head>
<body>

<h1 class="board-title">tilmorex.site</h1>
<p class="board-label label-home">Homepage</p>
<p class="board-label label-listing">listing</p>

<section class="page page-home">
  <header class="abs hero dark">
    <nav class="nav">
      <span class="nav-logo">TILMOREX.SITE</span>
      <span>Buy Domains</span><span>Sell Domains</span><span>Help</span><span>Login</span>
      <span class="nav-btn">Start</span>
    </nav>
    <h2 class="hero-title">Claim Your Space<br>In The Digital World</h2>
    <p class="copy hero-copy">Find the right name and start your brand today.</p>
    <div class="hero-search"><span class="btn">Search</span></div>
    <div class="art hero-art" role="img" aria-label="Isometric illustration of floating web pages"></div>
    <svg class="wave" style="bottom:0" viewBox="0 0 296 30" height="30" preserveAspectRatio="none"><path d="M0 18 C80 40 160 0 296 14 L296 30 L0 30 Z" fill="#fff"/></svg>
  </header>

  <div class="abs features">
    <article class="feature">
      <div class="icon" style="background:var(--orange)"></div>
      <h3>Trusted Transactions</h3>
      <p>Safe and simple payment for every sale.</p>
    </article>
    <article class="feature feature-main">
      <div class="icon" style="background:var(--white)"></div>
      <h3>Fast Transfers</h3>
      <p>Most domains move to you within a day.</p>
    </article>
    <article class="feature">
      <div class="icon" style="background:var(--green)"></div>
      <h3>Premium Names</h3>
      <p>Short names hand picked for brands.</p>
    </article>
  </div>
  <div class="abs features-cta"><span class="btn">Learn More</span></div>

  <div class="art trade-art" role="img" aria-label="Illustration of a domain marketplace screen"></div>
  <div class="abs trade-text">
    <h2 class="section-title">Buy &amp; Sell <span class="accent">Domains.</span></h2>
    <p class="copy" style="margin-top:4px">List your names, reach buyers and close deals in a few clicks.</p>
    <div class="trade-item"><span class="dot" style="background:var(--blue)"></span><div><h4>Transparent Fees</h4><p class="copy">One flat rate on every sale.</p></div></div>
    <div class="trade-item"><span class="dot" style="background:var(--green)"></span><div><h4>Monthly Plans</h4><p class="copy">Let buyers pay over time.</p></div></div>
    <div class="trade-item"><span class="dot" style="background:var(--orange)"></span><div><h4>Secure Escrow</h4><p class="copy">Funds held until transfer is done.</p></div></div>
  </div>

  <div class="abs investors">
    <h2 class="section-title">Here For <span class="accent">Domain Investors</span> Too</h2>
    <p class="copy">Manage your whole portfolio, track offers and price names from one dashboard.</p>
    <span class="btn">Get Started</span>
  </div>
  <div class="art investors-art" role="img" aria-label="Isometric illustration of connected servers"></div>

  <footer class="abs home-footer dark">
    <svg class="wave" style="top:0" viewBox="0 0 296 30" height="30" preserveAspectRatio="none"><path d="M0 0 L296 0 L296 10 C200 34 90 2 0 22 Z" fill="#fff"/></svg>
    <div class="art cta-art" role="img" aria-label="Illustration of a glowing server tower"></div>
    <h2 class="cta-title">Build Your Online <span class="accent">Business</span></h2>
    <p class="copy cta-copy">Pick a name today and launch your site tomorrow.</p>
    <span class="btn cta-btn">Browse Domains</span>
    <div class="foot-cols">
      <div class="foot-col"><h5>Domains</h5><p>Buy Domains<br>Sell Domains<br>Pricing</p></div>
      <div class="foot-col"><h5>Help</h5><p>Support<br>Guides<br>FAQ</p></div>
      <div class="foot-col"><h5>Company</h5><p>About<br>Careers<br>Contact</p></div>
      <div class="foot-col"><h5>Follow</h5><div class="socials"><span></span><span></span><span></span></div></div>
    </div>
    <div class="foot-bar"><span>© 2024 TILMOREX.SITE All rights reserved</span><span>Terms · Privacy</span></div>
  </footer>
</section>

<section class="page page-listing">
  <header class="abs list-header dark">
    <nav class="nav">
      <span class="nav-logo">TILMOREX.SITE</span>
      <span>Buy Domains</span><span>Sell Domains</span><span>Help</span>
      <span class="nav-btn">Login</span>
    </nav>
    <div class="list-search"><span class="btn">Search</span></div>
    <svg class="wave" style="bottom:0" viewBox="0 0 288 40" height="40" preserveAspectRatio="none"><path d="M0 14 C70 44 150 -4 288 24 L288 40 L0 40 Z" fill="#fff"/></svg>
  </header>

  <aside class="abs filters">
    <div class="filter">
      <h5>Categories</h5>
      <div class="filter-row"><span class="box on"></span>All Categories</div>
      <div class="filter-row"><span class="box"></span>Business</div>
      <div class="filter-row"><span class="box"></span>Technology</div>
      <div class="filter-row"><span class="box"></span>Travel</div>
    </div>
    <div class="filter">
      <h5>Extension</h5>
      <div class="filter-row"><span class="box on"></span>.com</div>
      <div class="filter-row"><span class="box"></span>.site</div>
    </div>
    <div class="filter">
      <h5>Length</h5>
      <div class="range"></div>
      <div class="field">Min</div><div class="field">Max</div>
    </div>
    <div class="filter">
      <h5>Price</h5>
      <div class="range"></div>
      <div class="field">Min</div><div class="field">Max</div>
    </div>
    <div class="filter"><h5>Starting With</h5><div class="field">Letters</div></div>
    <div class="filter"><h5>Ending With</h5><div class="field">Letters</div></div>
  </aside>

  <div class="abs results">
    <div class="results-head">4,000 Results <span>Sort by: Relevance</span></div>
    <div class="result"><div><h6>parkloop.com</h6><p>$2,400</p></div><span class="btn">Buy Now</span></div>
    <div class="result"><div><h6>parkvela.com</h6><p>$1,850</p></div><span class="btn">Buy Now</span></div>
    <div class="result"><div><h6>smartparko.com</h6><p>$990</p></div><span class="btn">Buy Now</span></div>
    <div class="result"><div><h6>parkhaven.com</h6><p>$3,200</p></div><span class="btn">Buy Now</span></div>
    <div class="result"><div><h6>parknestly.site</h6><p>$640</p></div><span class="btn">Buy Now</span></div>
    <div class="result"><div><h6>parkzenix.com</h6><p>$1,120</p></div><span class="btn">Buy Now</span></div>
    <div class="result"><div><h6>cityparkly.com</h6><p>$2,050</p></div><span class="btn">Buy Now</span></div>
    <div class="result"><div><h6>parkmora.com</h6><p>$780</p></div><span class="btn">Buy Now</span></div>
    <div class="result"><div><h6>parkrise.com</h6><p>$4,500</p></div><span class="btn">Buy Now</span></div>
    <div class="result"><div><h6>parkquill.com</h6><p>$1,300</p></div><span class="btn">Buy Now</span></div>
  </div>

  <footer class="abs list-footer dark">
    <svg class="wave" style="top:0" viewBox="0 0 288 24" height="24" preserveAspectRatio="none"><path d="M0 0 L288 0 L288 8 C190 28 90 0 0 18 Z" fill="#fff"/></svg>
    <div class="foot-cols" style="top:34px">
      <div class="foot-col"><h5>Domains</h5><p>Buy Domains<br>Sell Domains<br>Pricing</p></div>
      <div class="foot-col"><h5>Help</h5><p>Support<br>Guides<br>FAQ</p></div>
      <div class="foot-col"><h5>Company</h5><p>About<br>Careers<br>Contact</p></div>
      <div class="foot-col"><h5>Follow</h5><div class="socials"><span></span><span></span><span></span></div></div>
    </div>
    <div class="foot-bar"><span>© 2024 TILMOREX.SITE All rights reserved</span><span>Terms · Privacy</span></div>
  </footer>
</section>

</body>
</html>
```